Enlargement project

We would like to create an enlargement of the attached business card design, so that we are able to print hi-res business cards from it,

The end result we are after is an illustrator template that contains hi-res graphics and text that we can edit to insert people's names, job titles, phone and email details

The two colours used within the design are:

Pantone 350 (green)
Panton 484 (red)

The fonts used are;

Futura Medium
Futura Bk BT Italic

Industry/Entity Type

Business

```html
<!DOCTYPE html>
<html lang="en">
<head>
<meta charset="utf-8">
<title>Lookout – Business Card</title>
<link rel="stylesheet" href="https://fonts.googleapis.com/css2?family=Jost:ital,wght@0,400;0,500;1,400&display=swap">
<style>
  :root {
    --brand-green: #215732;
    --brand-red: #c8352b;
    --card-white: #ffffff;
    --backdrop: #e6e6e4;
    --card-shadow: rgba(0, 0, 0, 0.18);
  }
  html, body {
    margin: 0;
    padding: 0;
    width: 1200px;
    height: 900px;
    overflow: hidden;
    background: var(--backdrop);
    font-family: "Jost", "Futura", sans-serif;
  }
  .business-card {
    position: absolute;
    left: 180px;
    top: 193px;
    width: 840px;
    height: 513px;
    background: var(--card-white);
    box-shadow: 0 10px 30px var(--card-shadow);
  }
  .brand {
    position: absolute;
    left: 52px;
    top: 56px;
    display: flex;
    align-items: center;
    gap: 14px;
  }
  .brand-name {
    font-size: 54px;
    font-weight: 500;
    color: var(--brand-green);
    letter-spacing: 0.5px;
    line-height: 1;
  }
  .brand-square {
    width: 96px;
    height: 96px;
    background: var(--brand-red);
  }
  .contact {
    position: absolute;
    left: 52px;
    color: var(--brand-green);
    font-size: 21px;
    font-weight: 400;
    line-height: 1.3;
    margin: 0;
  }
  .contact-address { top: 196px; }
  .contact-phones { top: 296px; }
  .contact-email { top: 382px; }
  .contact-phones .label { display: inline-block; width: 22px; }
  .person {
    position: absolute;
    left: 545px;
    top: 244px;
    color: var(--brand-red);
  }
  .person-name {
    font-size: 34px;
    font-weight: 400;
    margin: 0;
    line-height: 1.1;
  }
  .person-title {
    font-size: 21px;
    font-weight: 400;
    margin: 2px 0 0;
  }
  .website {
    position: absolute;
    right: 52px;
    bottom: 44px;
    color: var(--brand-green);
    font-size: 22px;
    font-weight: 500;
  }
</style>
</head>
<body>
  <main class="business-card">
    <div class="brand">
      <span class="brand-name">Lookout</span>
      <span class="brand-square" aria-hidden="true"></span>
    </div>

    <p class="contact contact-address">
      Suite 4, Level 2<br>
      48 Sample Road<br>
      Harbourview NSW 2000
    </p>

    <p class="contact contact-phones">
      <span class="label">t:</span> 02 7100 0000<br>
      <span class="label">f:</span> 02 7100 1111<br>
      <span class="label">d:</span> 02 7100 2222
    </p>

    <p class="contact contact-email">tcarver@lookout.it</p>

    <div class="person">
      <p class="person-name">Tom Carver</p>
      <p class="person-title">Technical Operations</p>
    </div>

    <span class="website">www.lookout.it</span>
  </main>
</body>
</html>
```